Flyer für Einladung zu einer Veranstaltung
Zielgruppe
Ich möchte mit dem Flyer Geschäftsführer/ leitende Mitarbeiter von Jobcentern (JC) zu zwei Veranstaltungen an zwei aufeinander folgenden Tagen zu einer Teilnahme 'verführen'.
Hauptziel ist für mich, dass die JC meine Vermittlungsseminare in 2017 buchen.
Dazu dient Veranstaltung Nr. 2. Hier präsentieren wir Vermittlungsstrategien, zeigen Ausschnitte aus dem Seminar usw. Zwei frühere Flyer für eine inhaltlich gleiche Veranstaltung lege ich im Anhang bei.
Die erste Veranstaltung dient dazu, die GF´s mit einem interessanten Thema zum Seminarort zu locken.
Dazu lautet das Thema 'Das Beste aus 51 Jobcentern' und beinhaltet eine übersicht aus Highlights und No-go Erlebnissen aus den unterschiedlichen Behörden.
Angefragt ist der Besuch des NRW-Ministers für Arbeit und Soziales, am späten Nachmittag haben wir für Interessierte eine Führung im Kornhügelarena organisiert.
Aufgabenstellung
Flyerfarben lila und orange, Welle; es soll auch Platz für eine Anmeldung oder Rückfrage sein.

```html
<!DOCTYPE html>
<html lang="de">
<head>
<meta charset="utf-8">
<title>Das Beste aus 51 Jobcentern – Einladung</title>
<link href="https://fonts.googleapis.com/css2?family=Jost:wght@400;500;600;700&display=swap" rel="stylesheet">
<style>
  :root {
    --orange: #d98f37;
    --purple: #7b5698;
    --white: #ffffff;
    --backdrop: #c4c4c4;
  }
  * { box-sizing: border-box; margin: 0; padding: 0; }
  html, body { width: 1200px; height: 900px; overflow: hidden; }
  body {
    background: var(--backdrop);
    font-family: "Jost", sans-serif;
    position: relative;
  }
  .card {
    position: absolute;
    top: 102px;
    width: 492px;
    height: 696px;
    background: var(--orange);
    overflow: hidden;
  }
  .card--front { left: 59px; }
  .card--back { left: 651px; }

  .wave { position: absolute; inset: 0; width: 100%; height: 100%; }

  .kicker {
    position: absolute; left: 19px; top: 18px;
    color: var(--white); font-weight: 600; font-size: 13.5px;
  }
  .headline {
    position: absolute; left: 19px;
    font-weight: 700; font-size: 34px; line-height: 1;
    padding: 2px 4px 0;
    letter-spacing: 0.3px;
  }
  .headline--first {
    top: 40px; background: var(--orange); color: var(--white);
    border: 2px solid var(--white);
  }
  .headline--second {
    top: 81px; background: var(--white); color: var(--purple);
  }

  .facts {
    position: absolute; right: 22px; top: 118px;
    display: flex; flex-direction: column; align-items: flex-end; gap: 5px;
  }
  .fact {
    color: var(--white); font-weight: 600; font-size: 13.5px;
    padding: 1px 4px; line-height: 19px;
  }
  .fact--orange { background: var(--orange); border: 1.5px solid var(--white); }
  .fact--purple { background: var(--purple); }

  .column {
    position: absolute; top: 262px; height: 351px;
    background: var(--white); color: var(--orange);
    font-size: 10.2px; line-height: 1.3;
    padding: 9px 9px;
  }
  .column--intro { left: 19px; width: 223px; }
  .column--topics { left: 252px; width: 219px; }
  .topics-title { margin-bottom: 12px; }
  .topics-list { list-style: none; }
  .topics-list li {
    position: relative; padding-left: 22px; margin-bottom: 11px;
  }
  .topics-list li::before {
    content: ""; position: absolute; left: 2px; top: 4px;
    width: 5px; height: 5px; border-radius: 50%; background: var(--orange);
  }

  .extra-day {
    position: absolute; left: 19px; top: 620px; width: 452px; height: 55px;
    background: var(--purple); color: var(--white);
    font-size: 10.2px; line-height: 1.3; padding: 8px 9px;
  }

  .back-art { position: absolute; inset: 0; width: 100%; height: 100%; }
  .back-art text { font-family: "Jost", sans-serif; }
  .title-text { font-weight: 700; font-size: 31px; fill: var(--white); letter-spacing: 0.5px; }
  .info-text { font-size: 9.6px; fill: var(--orange); }
  .label-text { font-size: 9px; fill: var(--orange); }
  .stamp-text { font-size: 8.5px; fill: var(--white); }
  .address-text { font-size: 10px; fill: var(--orange); }
  .check-text { font-size: 7.6px; fill: var(--white); }
</style>
</head>
<body>

<section class="card card--front" aria-label="Vorderseite der Einladung">
  <svg class="wave" viewBox="0 0 492 696" preserveAspectRatio="none" aria-hidden="true">
    <path d="M0,0 H492 V8 C430,14 360,40 300,80 C240,120 170,195 0,200 Z" fill="var(--purple)"/>
  </svg>

  <p class="kicker">Einladung zum Erfahrungsaustausch</p>
  <h1 class="headline headline--first">DAS BESTE AUS</h1>
  <h1 class="headline headline--second">51 JOBCENTER</h1>

  <div class="facts">
    <span class="fact fact--orange">Kosten: 165,—€</span>
    <span class="fact fact--purple">Wann: 21.09.2016 | ca 10-16 Uhr</span>
    <span class="fact fact--orange">Wo: Musterstr. 12 | 12345 Dortmund</span>
    <span class="fact fact--purple">Für wen: Geschäftsführer | leitende Angestellte</span>
  </div>

  <div class="column column--intro">
    <p>Früher dachte ich, wenn ich ein Jobcenter kenne, kenne ich alle. Heute sage ich: „Wenn jedes Jobcenter jedes Jobcenter kennen würde, dann hätten wir heute 20 Prozent weniger Hartz-IV-Empfänger.“ Hintergrund dieser Schlussfolgerungen ist, dass wir bundesweit in Behörden Jobcenter-Mitarbeiter in der Arbeitsvermittlung und im Arbeitgeberservice trainieren. Dabei vermitteln wir Methoden, die die Arbeitsvermittlung von Langzeitarbeitslosen effizienter, häufiger und dauerhafter machen.<br>
    Bei unseren Tätigkeiten und Einblicken in die Strukturen von 51 Jobcentern in NRW und von der Nordsee bis nach Niederbayern haben wir aber auch entdeckt, wie unterschiedlich die Jobcenter arbeiten. Manchmal würden kleinste Drehungen an Jobcenter-Stellschrauben genügen, um im Alltag ohne viel Aufwand sofortige Arbeitserleichterungen oder/ und mehr Vermittlungen zu erreichen. Ein enormes Sparpotential!<br>
    Ein Erfahrungsaustausch darüber ist das zentrale Tagesthema.</p>
  </div>

  <div class="column column--topics">
    <p class="topics-title">Tagesthema 21. September 2016:</p>
    <p class="topics-title">Die besten Gestaltungsideen<br>aus 51 Jobcentern</p>
    <ul class="topics-list">
      <li>Erste, zweite und dritte Eindrücke aus den Jobcentern</li>
      <li>Motivationsknöpfe für Mitarbeiter</li>
      <li>Befugnisse und Anweisungen – Sinn und Unsinn</li>
      <li>Vorhandene Ressourcen besser nutzen</li>
      <li>An welchen Punkten eine Aufgabenüberprüfung sinnvoll ist</li>
      <li>Wie das Vermittlungsgespräch ganz schnell zum Erfolg werden kann</li>
      <li>Welche Probleme verschiedene Jobcenter wie gemeistert haben</li>
      <li>Ursache, Wirkung, Ausrichtung</li>
    </ul>
  </div>

  <p class="extra-day">Wenn Sie auch noch zum zweiten Tag (Testseminar für die Vermittlungstage) bleiben wollen, dann haben wir am späten Nachmittag noch eine Stadionführung in der Kornhügelarena organisiert.</p>
</section>

<section class="card card--back" aria-label="Rückseite mit Antwortkarte">
  <svg class="back-art" viewBox="0 0 492 696">
    <!-- stamp field -->
    <rect x="19" y="19" width="79" height="77" fill="var(--purple)"/>
    <text class="stamp-text" transform="translate(38,30) rotate(90)">Bitte</text>
    <text class="stamp-text" transform="translate(48,30) rotate(90)">freimachen</text>
    <text class="stamp-text" transform="translate(58,30) rotate(90)">falls Marke</text>
    <text class="stamp-text" transform="translate(68,30) rotate(90)">zur Hand</text>

    <!-- address field -->
    <rect x="250" y="62" width="96" height="139" fill="var(--white)"/>
    <text class="address-text" transform="translate(264,80) rotate(90)">An:</text>
    <text class="address-text" transform="translate(287,80) rotate(90)">Max Mustermann</text>
    <text class="address-text" transform="translate(309,80) rotate(90)">Platzhalter Allee 1</text>
    <text class="address-text" transform="translate(331,80) rotate(90)">12345 Dortmund</text>

    <!-- title -->
    <rect x="14" y="489" width="35" height="187" fill="var(--purple)"/>
    <text class="title-text" transform="translate(43,668) rotate(-90)">DAS BESTE</text>
    <rect x="57" y="337" width="37" height="339" fill="var(--orange)" stroke="var(--white)" stroke-width="2"/>
    <text class="title-text" transform="translate(86,668) rotate(-90)">AUS 51 JOBCENTER</text>

    <!-- info panel -->
    <rect x="110" y="257" width="68" height="419" fill="var(--white)"/>
    <text class="info-text" transform="translate(127,668) rotate(-90)">Für Rückfragen stehen wir Ihnen jederzeit telefonisch zur Verfügung. Wenn</text>
    <text class="info-text" transform="translate(142,668) rotate(-90)">Sie sich jedoch gleich einen der begehrten Seminarplätze sichern wollen,</text>
    <text class="info-text" transform="translate(157,668) rotate(-90)">senden Sie uns schriftlich eine Buchung.</text>

    <!-- reply form -->
    <g stroke="var(--white)" stroke-width="1.5">
      <line x1="185" y1="257" x2="475" y2="257"/>
      <line x1="200" y1="283" x2="200" y2="676"/>
      <line x1="229" y1="283" x2="229" y2="676"/>
      <line x1="258" y1="283" x2="258" y2="676"/>
      <line x1="286" y1="283" x2="286" y2="676"/>
      <line x1="314" y1="283" x2="314" y2="676"/>
      <line x1="342" y1="283" x2="342" y2="676"/>
      <line x1="433" y1="283" x2="433" y2="676"/>
      <line x1="458" y1="283" x2="458" y2="676"/>
    </g>
    <g fill="var(--white)">
      <rect x="184" y="616" width="13" height="60"/>
      <rect x="213" y="610" width="13" height="66"/>
      <rect x="242" y="590" width="13" height="86"/>
      <rect x="270" y="618" width="13" height="58"/>
      <rect x="298" y="620" width="13" height="56"/>
      <rect x="326" y="624" width="13" height="52"/>
      <rect x="352" y="604" width="13" height="72"/>
      <rect x="417" y="604" width="13" height="72"/>
    </g>
    <text class="label-text" transform="translate(194,674) rotate(-90)">Vorname:</text>
    <text class="label-text" transform="translate(223,674) rotate(-90)">Nachname:</text>
    <text class="label-text" transform="translate(252,674) rotate(-90)">Strasse/Hausnr.</text>
    <text class="label-text" transform="translate(280,674) rotate(-90)">PLZ/Ort:</text>
    <text class="label-text" transform="translate(308,674) rotate(-90)">Telefon:</text>
    <text class="label-text" transform="translate(336,674) rotate(-90)">E-Mail:</text>
    <text class="label-text" transform="translate(362,674) rotate(-90)">Teilnahme:</text>
    <text class="label-text" transform="translate(427,674) rotate(-90)">Rückfragen:</text>

    <text class="check-text" transform="translate(381,593) rotate(-90)">○ Ich nehme an der Veranstaltung »Das Beste aus 51 Jobcentern« am</text>
    <text class="check-text" transform="translate(391,593) rotate(-90)">19.09.2016 in Dortmund teil.</text>
  </svg>
</section>

</body>
</html>
```